Crestline Gas and Plumbing Business Card Design

I am after a business card design for my plumbing business called 'Crestline Gas & Plumbing'. I do all types of plumbing and gas work and specialise in general maintenance plumbing. Would like to see designs using current logo

Industry/Entity Type

Plumbing

Contact Information for Business Card

Name - Dale Whitcombe
Phone number - 0455163027
Email - admin@crestlinegasandplumbing.example.com.au
ABN - 68204915336

```html
<!DOCTYPE html>
<html lang="en">
<head>
<meta charset="utf-8">
<title>Crestline Gas &amp; Plumbing – Business Card</title>
<link href="https://fonts.googleapis.com/css2?family=Exo:wght@400;600;700;800&display=swap" rel="stylesheet">
<style>
  :root {
    --backdrop: #7f7f7f;
    --card: #ffffff;
    --ink: #333333;
    --brand-blue: #1f5ff0;
    --brand-orange: #f7791f;
    --flame-yellow: #ffc21a;
    --flame-orange: #ff8a1e;
    --flame-red: #ff5a20;
  }
  * { margin: 0; padding: 0; box-sizing: border-box; }
  html, body {
    width: 981px; height: 1200px; overflow: hidden;
    background: var(--backdrop);
    font-family: "Exo", sans-serif;
  }
  .canvas { position: relative; width: 981px; height: 1200px; }
  .card {
    position: absolute; left: 75px; width: 830px; height: 486px;
    background: var(--card); overflow: hidden;
  }
  .card--front { top: 82px; }
  .card--back { top: 643px; }

  .brand {
    position: absolute; display: flex; align-items: center;
    color: var(--brand-blue); font-weight: 800; text-transform: uppercase;
    white-space: nowrap;
  }
  .brand__dot { border-radius: 50%; background: var(--brand-orange); flex: none; }
  .card--front .brand { left: 53px; top: 98px; font-size: 24px; gap: 14px; letter-spacing: 0.5px; }
  .card--front .brand__dot { width: 44px; height: 44px; }
  .card--back .brand { left: 0; right: 0; top: 214px; justify-content: center; font-size: 38px; gap: 20px; letter-spacing: 0.5px; }
  .card--back .brand__dot { width: 68px; height: 68px; }

  .contact { position: absolute; left: 50px; top: 240px; color: var(--ink); text-transform: uppercase; white-space: nowrap; }
  .contact__name { font-weight: 700; font-size: 32px; letter-spacing: 1.5px; line-height: 1; }
  .contact__line { font-size: 19px; letter-spacing: 1px; line-height: 1; }
  .contact__phone { margin-top: 40px; }
  .contact__abn { margin-top: 18px; }
  .contact__email { margin-top: 35px; font-size: 17px; letter-spacing: 0.4px; }

  .flame-art { position: absolute; right: 0; top: 0; width: 250px; height: 486px; }
</style>
</head>
<body>
<main class="canvas">
  <section class="card card--front">
    <div class="brand"><span class="brand__dot"></span>Crestline Gas &amp; Plumbing</div>

    <div class="contact">
      <h1 class="contact__name">Dale Whitcombe</h1>
      <p class="contact__line contact__phone">Phone No : 0455163027</p>
      <p class="contact__line contact__abn">ABN - 68204915336</p>
      <p class="contact__line contact__email">admin@crestlinegasandplumbing.example.com.au</p>
    </div>

    <svg class="flame-art" viewBox="0 0 250 486" role="img" aria-label="Decorative flame illustration in yellow and orange">
      <defs>
        <linearGradient id="flameTone" x1="0" y1="0" x2="0" y2="1">
          <stop offset="0" stop-color="var(--flame-yellow)"/>
          <stop offset="0.55" stop-color="var(--flame-orange)"/>
          <stop offset="1" stop-color="var(--flame-red)"/>
        </linearGradient>
        <linearGradient id="flameFade" x1="0" y1="0" x2="1" y2="0">
          <stop offset="0" stop-color="#fff" stop-opacity="0"/>
          <stop offset="0.45" stop-color="#fff" stop-opacity="1"/>
        </linearGradient>
        <mask id="flameMask">
          <rect width="250" height="486" fill="url(#flameFade)"/>
        </mask>
      </defs>
      <rect width="250" height="486" fill="url(#flameTone)" mask="url(#flameMask)"/>
    </svg>
  </section>

  <section class="card card--back">
    <div class="brand"><span class="brand__dot"></span>Crestline Gas &amp; Plumbing</div>
  </section>
</main>
</body>
</html>
```